Signs to Go on the Side of Shipping Containers

We are a startup in North Alabama that will lease/sale shipping containers as Portable Storage options for business/construction sites. We need signs that will be mass produced and be mounted on every side of the container for advertising/visibility.
We need multiple sizes depending on the side the sign will be on/ the size of the container it is being mounted on.
Website: www.brindlecrestboxes.com

MUST BE SIMPLE AND EASY TO READ. Not to Busy. See example in
Updates

One designer is asking me to extend deadline. This is my first design project so not sure why they want me to do this but figured I would.

Target Market(s)

Business owners/Construction Companies/Individuals Moving

Industry/Entity Type

Portable Storage

Colors
0054AA
0677BA
7BADD7
CADEEF
E8F1F8

Requirements
Must have
• Company Name(Brindle Crest Boxes)/Phone Number (256-489-3172)/Website (www.brindlecrestboxes.com
Nice to have
• Play on the container shapes/pattern.

```html
<!DOCTYPE html>
<html lang="en">
<head>
<meta charset="utf-8">
<title>Brindle Crest Boxes – Container Sign</title>
<link rel="stylesheet" href="https://fonts.googleapis.com/css2?family=Barlow+Condensed:wght@600;700;800&family=Barlow+Semi+Condensed:wght@500;700&family=Montserrat:wght@700&display=swap">
<style>
  :root {
    --frame-grey: #b5b5b5;
    --paper: #ffffff;
    --navy: #162e40;
    --brand-blue: #0677ba;
    --ink: #111111;
  }
  html, body {
    margin: 0;
    padding: 0;
    width: 1200px;
    height: 1200px;
    overflow: hidden;
    background: var(--frame-grey);
  }
  .sign {
    position: relative;
    width: 1200px;
    height: 1200px;
    background: var(--frame-grey);
  }
  .sign__panel {
    position: absolute;
    left: 29px;
    top: 48px;
    width: 1128px;
    height: 1128px;
    background: var(--paper);
  }
  .brand {
    position: absolute;
    left: 148px;
    top: 128px;
    width: 900px;
    height: 240px;
  }
  .brand__mark {
    position: absolute;
    left: 0;
    top: 8px;
    width: 220px;
    height: 220px;
    background: var(--brand-blue);
  }
  .brand__name {
    position: absolute;
    left: 264px;
    top: 0;
    margin: 0;
    font-family: "Barlow Condensed", sans-serif;
    font-weight: 800;
    font-size: 104px;
    line-height: 0.92;
    color: var(--brand-blue);
    text-transform: uppercase;
    letter-spacing: 0.5px;
  }
  .brand__tagline {
    position: absolute;
    left: 360px;
    top: 198px;
    margin: 0;
    font-family: "Montserrat", sans-serif;
    font-weight: 700;
    font-size: 33px;
    letter-spacing: 0.3em;
    color: var(--ink);
    text-transform: uppercase;
  }
  .offer {
    position: absolute;
    left: 48px;
    top: 428px;
    width: 1090px;
    height: 398px;
    background: var(--navy);
  }
  .offer__headline {
    position: absolute;
    left: 92px;
    top: 66px;
    margin: 0;
    font-family: "Barlow Condensed", sans-serif;
    font-weight: 700;
    font-size: 186px;
    line-height: 1;
    color: var(--paper);
    letter-spacing: 1px;
  }
  .offer__subline {
    position: absolute;
    left: 92px;
    top: 236px;
    margin: 0;
    font-family: "Barlow Semi Condensed", sans-serif;
    font-weight: 700;
    font-size: 82px;
    line-height: 1;
    letter-spacing: 0.08em;
    color: var(--brand-blue);
  }
  .contact {
    position: absolute;
    left: 140px;
    top: 836px;
    margin: 0;
    font-family: "Barlow Semi Condensed", sans-serif;
    font-weight: 700;
    font-size: 104px;
    line-height: 1;
    letter-spacing: 0.05em;
    white-space: nowrap;
  }
  .contact__label { color: var(--navy); }
  .contact__number { color: var(--brand-blue); }
  .web {
    position: absolute;
    left: 48px;
    top: 950px;
    width: 1090px;
    height: 206px;
    background: var(--navy);
  }
  .web__address {
    position: absolute;
    left: 92px;
    top: 22px;
    margin: 0;
    font-family: "Barlow Semi Condensed", sans-serif;
    font-weight: 500;
    font-size: 58px;
    line-height: 1;
    letter-spacing: 0.085em;
    color: var(--paper);
  }
</style>
</head>
<body>
  <main class="sign">
    <div class="sign__panel"></div>

    <header class="brand">
      <div class="brand__mark" aria-hidden="true"></div>
      <h1 class="brand__name">Brindle Crest<br>Boxes</h1>
      <p class="brand__tagline">Sales &amp; Rentals</p>
    </header>

    <section class="offer">
      <h2 class="offer__headline">BUY OR RENT</h2>
      <p class="offer__subline">SHIPPING CONTAINERS</p>
    </section>

    <p class="contact">
      <span class="contact__label">CALL-</span><span class="contact__number">(256) 489-3172</span>
    </p>

    <footer class="web">
      <p class="web__address">www.brindlecrestboxes.com</p>
    </footer>
  </main>
</body>
</html>
```